Business card and stationary package

Travel management company looking for designs for single sided business cards, letterhead and envelope. Looking for contemporary designs using our existing logo. Design should clean, not trendy, no gradation of colors and no graphic other than the icon from the logo. Nothing complicated or difficult to read. Should be a crisp design using blue, gray and black colors only.
Letterhead should include a Word template and PDF template.
Business cards are one sided as the reverse will be dynamic images in our company portfolio of images.
We will use the same designer periodically for design projects using the same style guide for upcoming projects as well. Prefer working with designer that will assist with website, brochures and other marketing materials.

Logo Colors and Font:
Blue: 2189c6 Color Hex
Gray: 666666 Color Hex 60% Black
Black: 100% Black
Font: Century Gothic

Target Market(s)

business-to-business

Industry/Entity Type

Travel Industry

Contact Information for Business Card

Sample information for business cards will be:

Daniel Fenwick
Managing Partner

Harborline Journey Services, Inc.
274 Alder Lane, Suite 3621
Saco, ME 04072

207-555-0148 Direct Dial
207-555-0193 Fax

daniel@harborlinejourney.net
www.harborlinejourney.net

Font styles to use
Sans Serif

Requirements
Must have
• Clean, crisp design, easy to ready, memorable.
Nice to have
• We tend to like dynamic designs that are simple, not trendy, contemporary and easy to read.
Should not have
• no gradation of colors and no graphic other than the icon from the logo, no background images
• **Note that the background should only be white. No black/gary backgrounds or graded colors**

```html
<!DOCTYPE html>
<html lang="en">
<head>
<meta charset="utf-8">
<title>Harborline Journey Services – Business Card</title>
<link rel="stylesheet" href="https://fonts.googleapis.com/css2?family=Questrial&family=Roboto:wght@400&display=swap">
<style>
  :root {
    --brand-blue: #2189c6;
    --brand-gray: #666666;
    --text-gray: #555555;
    --card-white: #ffffff;
    --backdrop: #ececec;
  }
  * { box-sizing: border-box; margin: 0; padding: 0; }
  html, body {
    width: 1200px; height: 1200px; overflow: hidden;
    background: var(--backdrop);
  }
  .canvas { position: relative; width: 1200px; height: 1200px; }

  .card {
    position: absolute;
    width: 713px; height: 419px;
    background: var(--card-white);
    overflow: hidden;
  }
  .card--front { left: 238px; top: 119px; }
  .card--back  { left: 230px; top: 644px; }

  .wordmark {
    position: absolute;
    display: flex; align-items: center;
  }
  .wordmark__dot {
    flex: none;
    border-radius: 50%;
    background: var(--brand-blue);
  }
  .wordmark__name {
    font-family: "Questrial", "Century Gothic", sans-serif;
    color: var(--brand-gray);
    text-transform: uppercase;
    line-height: 1.1;
    white-space: nowrap;
  }

  .card--front .wordmark { left: 137px; top: 160px; }
  .card--front .wordmark__dot { width: 96px; height: 96px; margin-right: 24px; }
  .card--front .wordmark__name { font-size: 32px; letter-spacing: 2px; }

  .card--back .wordmark { left: 62px; top: 174px; }
  .card--back .wordmark__dot { width: 70px; height: 70px; margin-right: 16px; }
  .card--back .wordmark__name { font-size: 20px; letter-spacing: 1px; }

  .contact {
    position: absolute; left: 416px; top: 86px;
    font-family: "Roboto", Arial, sans-serif;
    color: var(--text-gray);
  }
  .contact__name {
    font-family: "Questrial", "Century Gothic", sans-serif;
    color: var(--brand-blue);
    font-size: 29px; line-height: 34px;
  }
  .contact__title { font-size: 16px; line-height: 22px; margin-bottom: 30px; }
  .contact__list { list-style: none; }
  .contact__item {
    display: flex; align-items: center;
    font-size: 18px; line-height: 25px;
  }
  .contact__icon {
    width: 17px; height: 17px; margin-right: 18px;
    fill: var(--brand-blue); flex: none;
  }
  .contact__address { font-size: 18px; line-height: 25px; margin-top: 2px; }
</style>
</head>
<body>
<main class="canvas">

  <section class="card card--front" aria-label="Business card front">
    <div class="wordmark">
      <span class="wordmark__dot"></span>
      <span class="wordmark__name">Harborline<br>Journey Services</span>
    </div>
  </section>

  <section class="card card--back" aria-label="Business card contact side">
    <div class="wordmark">
      <span class="wordmark__dot"></span>
      <span class="wordmark__name">Harborline<br>Journey Services</span>
    </div>

    <div class="contact">
      <p class="contact__name">Daniel Fenwick</p>
      <p class="contact__title">Managing Partner</p>
      <ul class="contact__list">
        <li class="contact__item">
          <svg class="contact__icon" viewBox="0 0 16 16" aria-hidden="true"><path d="M2 5c0-1.5 2.5-3 6-3s6 1.5 6 3v1.5h-3.2V5.2H5.2v1.3H2z"/><path d="M4 8l1.5-1.5h5L12 8v5H4z"/></svg>
          207-555-0148
        </li>
        <li class="contact__item">
          <svg class="contact__icon" viewBox="0 0 16 16" aria-hidden="true"><rect x="4" y="1.5" width="8" height="3.5"/><path d="M1.5 6h13v6H12v-2.5H4V12H1.5z"/><rect x="4.8" y="10.3" width="6.4" height="4.2"/></svg>
          207-555-0193
        </li>
        <li class="contact__item">
          <svg class="contact__icon" viewBox="0 0 16 16" aria-hidden="true"><path d="M1 3.5h14v1L8 9 1 4.5z"/><path d="M1 6l7 4.5L15 6v6.5H1z"/></svg>
          daniel@harborlinejourney.net
        </li>
        <li class="contact__item">
          <svg class="contact__icon" viewBox="0 0 16 16" aria-hidden="true"><path d="M8 1a7 7 0 1 0 0 14A7 7 0 0 0 8 1zm0 1.3c.8.9 1.4 2.4 1.6 4H6.4C6.6 4.7 7.2 3.2 8 2.3zM2.4 7.3h2.7c.1-1.5.5-2.9 1.1-3.9A5.7 5.7 0 0 0 2.4 7.3zm8.5 0h2.7a5.7 5.7 0 0 0-3.8-3.9c.6 1 1 2.4 1.1 3.9zM6.4 8.7h3.2c-.2 1.6-.8 3.1-1.6 4-.8-.9-1.4-2.4-1.6-4zm-4 0a5.7 5.7 0 0 0 3.8 3.9c-.6-1-1-2.4-1.1-3.9zm8.5 0c-.1 1.5-.5 2.9-1.1 3.9a5.7 5.7 0 0 0 3.8-3.9z"/></svg>
          www.harborlinejourney.net
        </li>
      </ul>
      <p class="contact__address">274 Alder Lane, Suite 3621<br>Saco, ME 04072</p>
    </div>
  </section>

</main>
</body>
</html>
```